We need a web design for a retail food business based in Greater Western Sydney Australia called Golden Lantern Noodle Restaurant. Basically just need a simple yet easily to navigate website to browse through a menu, gallery , brief description about us, opening hours.
Menu and Gallery will be constantly updated.
Will provide own images for gallery
Updates
Menu has been uploaded and some idea on the colours I would like on the site
Some additional pictures added to see what designs you guys can come up with . Thanks again
To All Designers,
Any extra fee on top of the designs that feels need to be charged, please let me know in advance
Reason: Extending Deadline as I have yet to find a design that I would like...Thanks guys
Target Market(s)
All groups
Industry/Entity Type
Business
Requirements
Must have
- Open minded to any designs
Nice to have
- Would like slideshow behind main logo.
Preferred light coloured site yet not too playful
Should not have
- Preferably no dark colours backgrounds

```html
<!DOCTYPE html>
<html lang="en">
<head>
<meta charset="utf-8">
<title>Golden Lantern Noodle Restaurant</title>
<link rel="stylesheet" href="https://fonts.googleapis.com/css2?family=Cabin:wght@400;500;600&display=swap">
<style>
  :root {
    --page-bg: #f1f1f1;
    --brand-red: #b30606;
    --button-red: #b3181b;
    --panel-dark: #2a2a2a;
    --ink-dark: #3b3b3b;
    --ink-mid: #5a5a5a;
    --ink-soft: #7a7a7a;
    --white: #ffffff;
    --card-border: #e1e1e1;
    --band-top: #d9d9d9;
  }
  * { margin: 0; padding: 0; box-sizing: border-box; }
  html, body { width: 1200px; height: 861px; overflow: hidden; }
  body {
    position: relative;
    background: var(--page-bg);
    font-family: "Cabin", "Gill Sans", sans-serif;
    color: var(--ink-dark);
  }
  .brand {
    position: absolute; top: 100px; left: 0; width: 1200px;
    display: flex; justify-content: center; align-items: center; gap: 14px;
  }
  .brand-dot { width: 26px; height: 26px; border-radius: 50%; background: var(--brand-red); }
  .brand-name { font-size: 36px; font-weight: 600; color: var(--ink-dark); letter-spacing: 0.3px; }

  .main-nav {
    position: absolute; left: 231px; top: 186px; width: 739px; height: 47px;
    background: var(--brand-red); border-radius: 12px 12px 0 0;
  }
  .main-nav a {
    position: absolute; top: 16px; color: var(--white); text-decoration: none;
    font-size: 15px; font-weight: 500; text-transform: uppercase; letter-spacing: 0.2px;
  }
  .nav-pointer {
    position: absolute; left: 283px; top: 232px; width: 0; height: 0;
    border-left: 6px solid transparent; border-right: 6px solid transparent;
    border-top: 9px solid var(--brand-red); z-index: 2;
  }

  .hero {
    position: absolute; left: 130px; top: 233px; width: 939px; height: 297px;
    background: var(--panel-dark); border-radius: 0 0 12px 12px;
  }
  .hero::before {
    content: ""; position: absolute; left: 0; top: 0; width: 101px; height: 12px;
    background: var(--panel-dark); border-radius: 12px 0 0 0;
  }
  .hero { border-top-left-radius: 12px; border-top-right-radius: 12px; }
  .slide-dots { position: absolute; left: 51px; top: 34px; display: flex; gap: 4px; }
  .slide-dots span { width: 14px; height: 14px; border-radius: 50%; background: #8a8a8a; }
  .slide-dots .is-active { background: var(--brand-red); border: 3px solid #1a1a1a; }
  .hero-title {
    position: absolute; left: 48px; top: 66px; font-size: 35px; font-weight: 400; color: var(--white);
  }
  .hero-text {
    position: absolute; left: 48px; top: 118px; width: 296px;
    font-size: 11px; line-height: 18px; color: var(--white); text-align: justify;
  }
  .btn {
    display: inline-block; position: absolute; background: var(--button-red); color: var(--white);
    font-size: 11.5px; text-align: center; text-decoration: none; border-radius: 2px;
    height: 24px; line-height: 24px; box-shadow: 0 1px 0 rgba(0,0,0,0.25);
  }
  .hero .btn-more { left: 50px; top: 236px; width: 76px; }
  .hero .btn-buy { left: 140px; top: 236px; width: 76px; line-height: 22px; }
  .hero-media {
    position: absolute; left: 455px; top: 22px; width: 450px; height: 249px;
    border: 5px solid var(--white);
    background: radial-gradient(ellipse at 40% 55%, #c9a066 0%, #9b8a56 30%, #d8d4cc 62%, #eeeeee 100%);
    box-shadow: 0 14px 16px -10px rgba(0,0,0,0.6);
  }
  .play-icon { position: absolute; left: 200px; top: 88px; }

  .feature-band {
    position: absolute; left: 0; top: 542px; width: 1200px; height: 200px;
    background: linear-gradient(var(--band-top), var(--page-bg));
  }
  .feature-card {
    position: absolute; top: 565px; width: 301px; height: 145px;
    background: var(--white); border: 1px solid var(--card-border);
    box-shadow: 0 14px 14px -12px rgba(0,0,0,0.25);
  }
  .feature-media {
    position: absolute; left: 14px; top: -1px; width: 111px; height: 145px;
    background: linear-gradient(135deg, #c2201f, #8e0d0d);
  }
  .feature-title {
    position: absolute; left: 137px; top: 19px; font-size: 18px; font-weight: 400;
    color: var(--ink-mid); text-transform: uppercase;
  }
  .feature-text {
    position: absolute; left: 137px; top: 50px; width: 143px;
    font-size: 11px; line-height: 18px; color: var(--ink-soft); text-align: justify;
  }
  .feature-card .btn { right: 16px; top: 110px; padding: 0 9px; }

  .site-footer {
    position: absolute; left: 0; top: 741px; width: 1200px; height: 120px;
    border-top: 1px solid #e4e4e4;
  }
  .social-links { position: absolute; left: 131px; top: 32px; display: flex; gap: 11px; }
  .social-links span {
    width: 41px; height: 41px; border-radius: 50%;
    background: linear-gradient(#ffffff, #ececec); border: 1px solid #dcdcdc;
  }
  .footer-nav {
    position: absolute; right: 132px; top: 28px; font-size: 11px; color: var(--ink-dark);
  }
  .footer-nav a { color: var(--ink-dark); text-decoration: none; }
  .footer-nav .sep { margin: 0 18px; }
  .copyright { position: absolute; right: 132px; top: 62px; font-size: 11px; color: var(--ink-dark); }
</style>
</head>
<body>
  <header class="brand">
    <span class="brand-dot"></span>
    <span class="brand-name">Golden Lantern Noodle Restaurant</span>
  </header>

  <nav class="main-nav">
    <a href="#" style="left:40px">Home</a>
    <a href="#" style="left:133px">Menu</a>
    <a href="#" style="left:224px">Gallery</a>
    <a href="#" style="left:336px">About us</a>
    <a href="#" style="left:457px">Opening hours</a>
    <a href="#" style="left:608px">Contact us</a>
  </nav>
  <div class="nav-pointer"></div>

  <section class="hero">
    <div class="slide-dots"><span class="is-active"></span><span></span><span></span><span></span></div>
    <h1 class="hero-title">Golden Lantern</h1>
    <p class="hero-text">Lorem ipsum dolor sit amet, consectetur adipisicing elit, sed do eiusmod tempor incididunt ut labore et dolore magna aliqua. Ut enim ad minim veniam, quis nostrud exercitation ullamco laboris nisi ut aliquip ex ea commodo consequat. Duis aute irure dolor in reprehenderit in voluptate velit esse cillum dolore eu fugiat nulla pariatur.</p>
    <a class="btn btn-more" href="#">View More</a>
    <a class="btn btn-buy" href="#">Buy Now</a>
    <div class="hero-media" role="img" aria-label="Video still of a bowl of noodle soup with chicken and vegetables">
      <svg class="play-icon" width="52" height="62" viewBox="0 0 52 62" aria-hidden="true">
        <path d="M2 2 L50 31 L2 60 Z" fill="#ffffff" opacity="0.92"/>
      </svg>
    </div>
  </section>

  <div class="feature-band"></div>

  <article class="feature-card" style="left:130px">
    <div class="feature-media" role="img" aria-label="Takeaway noodle box with chopsticks"></div>
    <h2 class="feature-title">Special offer</h2>
    <p class="feature-text">Lorem Ipsum has been the industry's standard dummy text ever since the 1500s.</p>
    <a class="btn" href="#">Buy Now</a>
  </article>

  <article class="feature-card" style="left:450px">
    <div class="feature-media" role="img" aria-label="Menu book icon with fork and spoon"></div>
    <h2 class="feature-title" style="left:133px">Our menu</h2>
    <p class="feature-text" style="left:135px">Lorem Ipsum has been the industry's standard dummy text ever since the 1500s.</p>
    <a class="btn" href="#">Order NOw</a>
  </article>

  <article class="feature-card" style="left:770px">
    <div class="feature-media" style="left:10px" role="img" aria-label="Bowl of stir-fried green beans with chopsticks"></div>
    <h2 class="feature-title" style="left:140px;top:22px">Today's special</h2>
    <p class="feature-text" style="left:140px">Lorem Ipsum has been the industry's standard dummy text ever since the 1500s.</p>
    <a class="btn" href="#">More Special</a>
  </article>

  <footer class="site-footer">
    <div class="social-links"><span></span><span></span><span></span><span></span></div>
    <nav class="footer-nav">
      <a href="#">Home</a><span class="sep">|</span><a href="#">Menu</a><span class="sep">|</span><a href="#">Gallery</a><span class="sep">|</span><a href="#">About us</a><span class="sep">|</span><a href="#">Opening hours</a><span class="sep">|</span><a href="#">Contact us</a>
    </nav>
    <p class="copyright">©2013 Golden Lantern Noodle Restaurant | All Rights Reserved</p>
  </footer>
</body>
</html>
```